Packaging label for launch of sun dried tomato products.

Established family farm in South Africa growing fruit for the production of dried fruit. We need a packaging label for the launch of our sun dried tomato products ie dried tomatoes in olive oil, dried tomato flakes and tomato powder. Packaging will be a round glass "jam jar" and spice shaker bottle. Due to limited amount of product available we cannot market to the masses, but rather focus on conveying a message of quality and exclusivity.

Target Market(s)

Home chef

Industry/Entity Type

Food

Font styles to use
Serif

Requirements
Nice to have
• Include the farm name in the design. TAVSONE

```html
<!DOCTYPE html>
<html lang="en">
<head>
<meta charset="utf-8">
<title>Tavsone Sun Dried Tomatoes in Olive Oil – Label</title>
<link rel="stylesheet" href="https://fonts.googleapis.com/css2?family=Playfair+Display:wght@700;800&family=Tinos:wght@400;700&display=swap">
<style>
  :root {
    --red: #cf131b;
    --red-deep: #a50c12;
    --white: #ffffff;
    --gold: #f2b01e;
    --tomato: #8e1a10;
    --tomato-dark: #4a0e08;
    --oil: #e9b62c;
    --leaf: #4d8a2e;
  }
  * { margin: 0; padding: 0; box-sizing: border-box; }
  html, body { width: 900px; height: 1200px; overflow: hidden; }
  body {
    position: relative;
    background: radial-gradient(ellipse at 40% 40%, var(--red) 0%, #c3111a 60%, var(--red-deep) 100%);
    color: var(--white);
    font-family: "Tinos", "Times New Roman", serif;
  }
  .ingredients {
    position: absolute; left: 24px; top: 28px; width: 470px;
    font-size: 29px; line-height: 36px;
  }
  .nutrition {
    position: absolute; left: 24px; top: 212px; width: 456px; height: 792px;
    border: 3px solid var(--white);
    padding: 14px 22px 0 22px;
    background: var(--red);
  }
  .nutrition__title { font-size: 50px; line-height: 58px; border-bottom: 3px solid var(--white); padding-bottom: 4px; }
  .nutrition__serving {
    display: flex; justify-content: space-between;
    font-size: 15px; margin-top: 30px; padding-bottom: 8px;
    border-bottom: 8px solid var(--white);
  }
  .nutrition__amount { font-size: 15px; margin-top: 8px; }
  .nutrition__calories {
    display: flex; justify-content: space-between; align-items: baseline;
    font-size: 46px; line-height: 50px; border-bottom: 4px solid var(--white); padding-bottom: 4px;
  }
  .nutrition__dv { font-size: 13px; margin: 14px 0 10px; }
  .facts { list-style: none; font-size: 14px; }
  .facts li {
    display: grid; grid-template-columns: 90px 1fr 60px;
    height: 27px; align-items: center;
  }
  .facts .val { text-align: right; }
  .facts .sub .name { padding-left: 40px; }
  .facts .gap { margin-top: 8px; }
  .nutrition__note {
    font-size: 12px; line-height: 16px; margin-top: 14px;
    border-top: 2px solid var(--white); padding-top: 8px;
  }
  .photo {
    position: absolute; left: 470px; top: 440px; width: 430px; height: 760px;
    border-radius: 40px 0 0 0;
    background:
      linear-gradient(200deg, var(--oil) 0%, rgba(233,182,44,0.55) 22%, rgba(142,26,16,0.35) 45%, var(--tomato) 72%, var(--tomato-dark) 100%);
  }
  .brand {
    position: absolute; left: 676px; top: 206px;
    display: flex; align-items: center; gap: 8px;
  }
  .brand__mark { width: 14px; height: 14px; background: var(--gold); }
  .brand__name {
    font-family: "Tinos", serif; font-weight: 700; font-size: 22px; letter-spacing: 1px;
    color: var(--gold);
  }
  .product-title {
    position: absolute; left: 500px; top: 262px; width: 350px; text-align: center;
    font-family: "Playfair Display", Georgia, serif; font-weight: 800;
    font-size: 66px; line-height: 68px;
  }
  .product-subtitle {
    position: absolute; left: 500px; top: 404px; width: 350px; text-align: center;
    font-size: 27px; letter-spacing: 1px;
  }
  .contact {
    position: absolute; left: 384px; top: 1056px; width: 426px; height: 120px;
    border: 3px solid var(--white);
    display: flex; align-items: center; justify-content: center; text-align: center;
    font-weight: 700; font-size: 21px; line-height: 28px;
    background: var(--red);
  }
</style>
</head>
<body>
  <p class="ingredients">Ingredient:Sun dried tomato, Olive oil, water, Basil, Crushed red pepper, Mint, marjoram.</p>

  <div class="photo" role="img" aria-label="Photo of olive oil pouring onto a bowl of sun dried tomatoes with fresh basil leaves"></div>

  <section class="nutrition">
    <h2 class="nutrition__title">Nutrition Facts</h2>
    <div class="nutrition__serving"><span>Serving size</span><span>1/4 cup (35g)</span></div>
    <p class="nutrition__amount">Amount Per Serving</p>
    <div class="nutrition__calories"><span>Calories</span><span>190</span></div>
    <p class="nutrition__dv">% Daily Value*</p>
    <ul class="facts">
      <li><span></span><span class="name">Total Fat</span><span class="val"></span></li>
      <li class="sub"><span>25%</span><span class="name">Saturated Fat</span><span class="val">15g</span></li>
      <li class="sub"><span>25%</span><span class="name">Trans Fat</span><span class="val">15g</span></li>
      <li class="sub"><span>25%</span><span class="name">Polyunsaturated Fat</span><span class="val">15g</span></li>
      <li class="sub"><span>25%</span><span class="name">Monounsaturated Fat</span><span class="val">15g</span></li>
      <li><span>1%</span><span class="name">Cholesterol</span><span class="val">10mg</span></li>
      <li><span>1%</span><span class="name">Sodium</span><span class="val">10mg</span></li>
      <li><span>1%</span><span class="name">Total Carbohydrate</span><span class="val">10g</span></li>
      <li class="sub"><span></span><span class="name">Dietary Fiber</span><span class="val">4g</span></li>
      <li class="sub"><span>0%</span><span class="name">Sugars</span><span class="val">4g</span></li>
      <li class="sub"><span>0%</span><span class="name">Polyalcohols</span><span class="val">4g</span></li>
      <li><span>0%</span><span class="name">Protein</span><span class="val">4g</span></li>
      <li class="gap"><span>5%</span><span class="name">Vitamin A</span><span class="val">5g</span></li>
      <li><span>5%</span><span class="name">Vitamin C</span><span class="val">5g</span></li>
      <li><span>5%</span><span class="name">Calcium</span><span class="val">5g</span></li>
      <li><span>5%</span><span class="name">Iron</span><span class="val">5g</span></li>
    </ul>
    <p class="nutrition__note">* Percent Daily Values are based on a 2,000 calorie diet. Your daily values may be higher or lower depending on your calorie needs</p>
  </section>

  <div class="brand"><span class="brand__mark"></span><span class="brand__name">TAVSONE</span></div>
  <h1 class="product-title">sun dried tomatoes</h1>
  <p class="product-subtitle">IN OLIVE OIL</p>

  <div class="contact">SPACE FOR COMPANY NAME,<br>ADDRESS AND CONTACT<br>INFORMATION</div>
</body>
</html>
```